Webpage for a treatment housing for young addicts.

I need a new design and files for my wordpress page. I need it to be more neat and clean. I need it to look professional with a starting page that will work as a navigation. I need like logo and phone number and such up top, a picture under it with one sentence as a slogan and under it 6 boxes to click to come to our different pages. Under it I want news etc.

Target Market(s)

Social services, employees and governements

Coding

Coded - Design and coding required

Font styles to use
Sans Serif

Colors
abd037
3176b5
9d9d9d
aaaaaa
f04a50

Requirements
Must have
• A nice design
Nice to have
• need it to look professional with a starting page that will work as a navigation. I need like logo and phone number and such up top, a picture under it with one sentence as a slogan and under it 6 boxes to click to come to our different pages. Under it I want news etc.
• today www.kolrev.se
• want more like www.tralvik.se or www.bersona.se
Should not have
• To many different colours and a messy design.

```html
<!DOCTYPE html>
<html lang="en">
<head>
<meta charset="utf-8">
<title>Kolrev – Care and housing</title>
<link href="https://fonts.googleapis.com/css2?family=Jost:wght@400;500;600&display=swap" rel="stylesheet">
<style>
:root{
  --blue:#0a7fcf;
  --blue-dark:#0b6fb6;
  --red:#f04a50;
  --green:#abd037;
  --ink:#2d2f33;
  --text:#55585d;
  --muted:#9d9d9d;
  --line:#e4e6ea;
  --panel:#e7e9ed;
  --slate:#464a51;
  --card:#f1f2f4;
  --white:#fff;
}
*{box-sizing:border-box;margin:0;padding:0}
html,body{width:1200px;height:3103px;overflow:hidden}
body{font-family:"Jost",sans-serif;color:var(--text);background:var(--white);position:relative}
a{color:inherit;text-decoration:none}
.wrap{width:1040px;margin:0 auto;position:relative}

/* header */
.site-header{height:80px;display:flex;align-items:center;justify-content:space-between;padding-left:80px;background:var(--white);box-shadow:0 2px 6px rgba(0,0,0,.06);position:relative;z-index:2}
.brand{display:flex;align-items:center;gap:10px;font-size:30px;font-weight:600;color:var(--blue)}
.brand-dot{width:28px;height:28px;border-radius:50%;background:var(--green)}
.header-tools{display:flex;height:80px}
.tool{display:flex;align-items:center;justify-content:center;gap:10px;border-left:1px solid var(--line);padding:0 20px;font-size:13px;color:var(--ink);white-space:nowrap}
.tool svg{stroke:var(--red);fill:none;stroke-width:2;flex:none}
.tool.call{width:196px}
.call small{display:block;color:var(--red);font-size:13px;line-height:1.1}
.call b{display:block;font-size:18px;font-weight:500;color:var(--ink);line-height:1.2}
.tool.stack{flex-direction:column;gap:4px;width:142px}
.tool.search{width:80px}
.tool.menu{width:80px}

/* hero */
.hero{height:360px;background:radial-gradient(circle at 80% 45%,#7a4a3a 0,#a77c62 22%,transparent 45%),linear-gradient(100deg,#c9b9a6 0%,#b79676 40%,#8f6a52 70%,#d6c9bb 100%);position:relative}
.hero::after{content:"";position:absolute;inset:0;background:rgba(30,25,20,.35)}
.hero-title{position:absolute;top:138px;left:0;right:0;text-align:center;color:var(--white);font-size:36px;font-weight:500;line-height:44px;z-index:1}
.hero-arrow{position:absolute;left:592px;top:306px;z-index:1}

/* tiles */
.tiles{background:var(--panel);height:270px;padding-top:63px}
.tile-grid{display:grid;grid-template-columns:repeat(3,336px);gap:16px 16px;justify-content:space-between}
.tile{height:64px;background:var(--white);display:flex;align-items:center;justify-content:space-between;padding:0 24px;font-size:15px;font-weight:500;color:var(--ink)}
.tile svg{stroke:var(--red);fill:none;stroke-width:1.6}
.tile.is-active{color:var(--red);box-shadow:0 6px 16px rgba(0,0,0,.12)}

/* intro */
.intro{height:382px;text-align:center;padding-top:68px}
.intro h1{font-size:24px;font-weight:500;color:var(--ink);line-height:30px}
.intro p{width:660px;margin:26px auto 0;font-size:13px;line-height:21px;color:var(--muted)}
.btn-outline{display:inline-block;margin-top:34px;border:2px solid var(--red);color:var(--red);font-size:12px;font-weight:500;padding:7px 22px}
.btn-solid{display:inline-block;background:var(--red);color:var(--white);font-size:12px;font-weight:500;padding:9px 24px}

/* feature band */
.features{background:var(--blue);height:338px;padding-top:65px}
.feature-grid{display:flex;justify-content:space-between}
.feature{width:320px;height:200px;position:relative}
.feature span{position:absolute;left:24px;bottom:22px;color:var(--white);font-size:15px;font-weight:500}
.feature svg{position:absolute;right:22px;bottom:24px;stroke:var(--white);fill:none;stroke-width:2}
.f-team{background:linear-gradient(160deg,#7f9a4a,#b19470 60%,#5d6b3a)}
.f-quality{background:linear-gradient(160deg,#6e5a4a,#c9b7a5 50%,#5a4a40)}
.f-values{background:linear-gradient(160deg,#5a3a28,#b3643f 50%,#7a4a2c)}
.feature .underline{text-decoration:underline}

/* two columns */
.duo{height:401px;display:flex;position:relative}
.duo::before{content:"";position:absolute;left:600px;top:48px;bottom:50px;width:1px;background:var(--line)}
.duo-col{width:50%;text-align:center;padding-top:88px}
.duo-col h2{font-size:36px;font-weight:500;color:var(--ink);line-height:44px}
.duo-col p{width:420px;margin:22px auto 0;font-size:12.5px;line-height:19px;color:var(--muted)}
.duo-col .btn-outline,.duo-col .btn-solid{margin-top:28px}

/* locations */
.locator{background:var(--slate);height:238px;text-align:center;padding-top:42px}
.locator h2{color:var(--white);font-size:36px;font-weight:500}
.locator p{color:var(--white);font-size:13px;margin-top:6px}
.locator-form{display:flex;justify-content:center;gap:18px;margin-top:30px}
.select{width:270px;height:40px;background:var(--white);display:flex;align-items:center;justify-content:space-between;padding:0 16px;font-size:12px;color:var(--muted)}
.select svg{stroke:var(--muted);fill:none;stroke-width:1.5}
.locator .btn-solid{width:136px;height:40px;padding:0;line-height:40px}

/* articles */
.articles{height:652px;text-align:center;padding-top:60px}
.articles h2{font-size:36px;font-weight:500;color:var(--ink);line-height:44px}
.articles .sub{font-size:13px;color:var(--text);margin-top:2px}
.article-grid{display:flex;justify-content:space-between;margin-top:30px}
.article{width:320px;height:317px;background:var(--card)}
.article-img{height:200px}
.a1{background:linear-gradient(150deg,#8fb4d0,#e9c9a6 55%,#d2a34c)}
.a2{background:linear-gradient(150deg,#dfe3e5,#c7b3a0 55%,#a8a7a4)}
.a3{background:linear-gradient(150deg,#eef0ef,#c59f83 55%,#8a7a66)}
.article time{display:block;font-size:12px;color:var(--ink);margin-top:22px}
.article h3{font-size:15px;font-weight:500;color:var(--blue-dark);line-height:19px;margin-top:10px;padding:0 34px}
.article h3.linked{text-decoration:underline}
.dots{display:flex;justify-content:center;gap:14px;margin-top:30px}
.dots i{width:12px;height:12px;border:2px solid var(--red);border-radius:50%}
.dots i.on{background:radial-gradient(circle,var(--red) 2px,transparent 3px)}
.articles .btn-solid{margin-top:24px}

/* footer */
.site-footer{background:var(--blue);height:382px;color:var(--white);position:absolute;left:0;right:0;top:2721px}
.footer-cols{display:flex;padding-top:58px}
.footer-col{width:268px;font-size:13px;line-height:24px}
.footer-col h4{font-size:17px;font-weight:500;margin-bottom:22px}
.footer-col .big{font-size:18px;font-weight:500}
.footer-col .label{font-weight:600;margin-top:14px}
.footer-col .current{text-decoration:underline}
.newsletter{width:252px;height:32px;background:rgba(255,255,255,.3);margin-top:16px;display:flex;align-items:center;justify-content:space-between;padding:0 14px;font-size:11px;color:rgba(255,255,255,.8)}
.newsletter svg{stroke:var(--white);fill:none;stroke-width:1.6}
.footer-bottom{position:absolute;left:0;right:0;top:304px;border-top:1px solid rgba(255,255,255,.3);height:78px}
.footer-bottom .wrap{display:flex;align-items:center;height:78px;font-size:13px}
.follow{position:absolute;left:536px;display:flex;align-items:center;gap:10px}
.follow i{width:24px;height:24px;border:2px solid var(--white);border-radius:50%}
.to-top{position:absolute;right:-40px;stroke:var(--white);fill:none;stroke-width:2}
</style>
</head>
<body>

<header class="site-header">
  <a class="brand" href="#"><span class="brand-dot"></span>Kolrev</a>
  <div class="header-tools">
    <div class="tool call">
      <svg width="24" height="24" viewBox="0 0 24 24"><path d="M5 3h4l2 5-3 2a12 12 0 0 0 6 6l2-3 5 2v4a2 2 0 0 1-2 2A17 17 0 0 1 3 5a2 2 0 0 1 2-2z"/></svg>
      <div><small>Call Us:</small><b>010-4417280</b></div>
    </div>
    <div class="tool stack">
      <svg width="26" height="20" viewBox="0 0 26 20"><rect x="1" y="1" width="24" height="18"/><path d="M1 1l12 10L25 1"/></svg>
      <span>info@kolrev.se</span>
    </div>
    <div class="tool stack search">
      <svg width="22" height="22" viewBox="0 0 24 24"><circle cx="13" cy="10" r="7"/><path d="M8 15l-6 6"/></svg>
      <span>Search</span>
    </div>
    <div class="tool menu">
      <svg width="28" height="20" viewBox="0 0 28 20"><path d="M0 2h28M0 10h28M0 18h28"/></svg>
    </div>
  </div>
</header>

<section class="hero" role="img" aria-label="Photo of a child playing with a toy car on the floor">
  <h2 class="hero-title">We create sustainable roads<br>to a better future</h2>
  <svg class="hero-arrow" width="16" height="22" viewBox="0 0 16 22" stroke="#fff" fill="none" stroke-width="2"><path d="M8 0v20M2 14l6 6 6-6"/></svg>
</section>

<section class="tiles">
  <nav class="wrap tile-grid">
    <a class="tile" href="#">Personal assistance<svg width="20" height="20" viewBox="0 0 20 20"><circle cx="10" cy="10" r="8"/><path d="M6 10h8M11 7l3 3-3 3"/></svg></a>
    <a class="tile is-active" href="#">Individual and family<svg width="20" height="20" viewBox="0 0 20 20"><circle cx="10" cy="10" r="8"/><path d="M6 10h8M11 7l3 3-3 3"/></svg></a>
    <a class="tile" href="#">LSS<svg width="20" height="20" viewBox="0 0 20 20"><circle cx="10" cy="10" r="8"/><path d="M6 10h8M11 7l3 3-3 3"/></svg></a>
    <a class="tile" href="#">Elderly care<svg width="20" height="20" viewBox="0 0 20 20"><circle cx="10" cy="10" r="8"/><path d="M6 10h8M11 7l3 3-3 3"/></svg></a>
    <a class="tile" href="#">About Kolrev<svg width="20" height="20" viewBox="0 0 20 20"><circle cx="10" cy="10" r="8"/><path d="M6 10h8M11 7l3 3-3 3"/></svg></a>
    <a class="tile" href="#">Investor<svg width="20" height="20" viewBox="0 0 20 20"><circle cx="10" cy="10" r="8"/><path d="M6 10h8M11 7l3 3-3 3"/></svg></a>
  </nav>
</section>

<section class="intro">
  <h1>Kolrev Sverige AB carries out care and care aimed<br>at people aged 14-25 years.</h1>
  <p>Kolrev Sverige AB carries out care and care aimed at people aged 14-25 years. This is done primarily through Home for care and housing (HVB). We are specialists in psychosocial abuse and crime issues. By being constantly open to new methods and aware of the existing ones, we develop and improve our care. The methods are adapted to the individual, we do not think that ONE thought or ONE perspective can be applied to everyone ...</p>
  <a class="btn-outline" href="#">Discover more</a>
</section>

<section class="features">
  <div class="wrap feature-grid">
    <a class="feature f-team" href="#" role="img" aria-label="Photo of a group of young people sitting together outdoors"><span>The team</span><svg width="10" height="16" viewBox="0 0 10 16"><path d="M2 2l6 6-6 6"/></svg></a>
    <a class="feature f-quality" href="#" role="img" aria-label="Photo of a carer helping an elderly woman"><span class="underline">Quality work</span><svg width="18" height="14" viewBox="0 0 18 14"><path d="M0 7h16M10 1l6 6-6 6"/></svg></a>
    <a class="feature f-values" href="#" role="img" aria-label="Photo of a mother and child watering plants"><span>Valuation &amp; Ethical Approach</span><svg width="10" height="16" viewBox="0 0 10 16"><path d="M2 2l6 6-6 6"/></svg></a>
  </div>
</section>

<section class="duo">
  <div class="duo-col">
    <h2>Almhaga farm<br>HVB</h2>
    <p>Close to Malmö, Lund and Helsingborg lies Almhagagården beautifully situated in the small village of Ekeby surrounded by beautiful nature and rolling fields ...</p>
    <a class="btn-outline" href="#">Explore more</a>
  </div>
  <div class="duo-col">
    <h2>In-depth description of<br>treatment.</h2>
    <p>The basis for treatment is a well-structured therapeutic treatment and housing environment, where the therapeutic environment becomes an active treatment layer ...</p>
    <a class="btn-solid" href="#">Explore more</a>
  </div>
</section>

<section class="wrap locator">
  <h2>We are located all over sweden!</h2>
  <p>There are many variations of passages of Lorem Ipsum</p>
  <form class="locator-form">
    <div class="select">Select country<svg width="10" height="6" viewBox="0 0 10 6"><path d="M1 1l4 4 4-4"/></svg></div>
    <div class="select">Choose service<svg width="10" height="6" viewBox="0 0 10 6"><path d="M1 1l4 4 4-4"/></svg></div>
    <span class="btn-solid">Search</span>
  </form>
</section>

<section class="wrap articles">
  <h2>Recent articles</h2>
  <p class="sub">There are many variations of passages of Lorem Ipsum</p>
  <div class="article-grid">
    <article class="article">
      <div class="article-img a1" role="img" aria-label="Photo of a mother and daughter building with toy blocks"></div>
      <time>November 13, 2018</time>
      <h3>Contrary to popular belief,Ipsum is not simply</h3>
    </article>
    <article class="article">
      <div class="article-img a2" role="img" aria-label="Photo of a carer embracing an elderly woman"></div>
      <time>October 18, 2018</time>
      <h3>Contrary to popular belief,Ipsum is not simply</h3>
    </article>
    <article class="article">
      <div class="article-img a3" role="img" aria-label="Photo of a carer serving a meal to an elderly woman"></div>
      <time>October 15, 2018</time>
      <h3 class="linked">Contrary to popular belief,Ipsum is not simply</h3>
    </article>
  </div>
  <div class="dots"><i></i><i class="on"></i><i></i></div>
  <a class="btn-solid" href="#">View all news</a>
</section>

<footer class="site-footer">
  <div class="wrap footer-cols">
    <div class="footer-col">
      <h4>Contact us</h4>
      <div class="big">Call us: 010-4417280</div>
      <div>Email: info@kolrev.se</div>
      <div class="label">Visit us:</div>
      <div>Ekeby 2208 24731 Lindås</div>
    </div>
    <div class="footer-col">
      <h4>Quick links</h4>
      <div>Personal assistance</div>
      <div class="current">Individual and family</div>
      <div>LSS</div>
      <div>Elderly care</div>
      <div>About Kolrev</div>
      <div>Investor</div>
    </div>
    <div class="footer-col">
      <h4>About Kolrev</h4>
      <div>The team</div>
      <div>Quality work</div>
      <div>Valuation &amp; Ethical Approach</div>
      <div>News</div>
    </div>
    <div class="footer-col">
      <h4>Sign up newsletter</h4>
      <div style="line-height:18px">Sign up now &amp; get Update about anything News!</div>
      <div class="newsletter">Enter your email ...<svg width="14" height="10" viewBox="0 0 14 10"><path d="M0 5h12M8 1l4 4-4 4"/></svg></div>
    </div>
  </div>
  <div class="footer-bottom">
    <div class="wrap">
      <span>© 2018 Kolrev. All rights reserved.</span>
      <div class="follow">Follow Us: <i></i><i></i><i></i></div>
      <svg class="to-top" width="16" height="18" viewBox="0 0 16 18"><path d="M2 16L8 2l6 14M4 11h8"/></svg>
    </div>
  </div>
</footer>

</body>
</html>
```